complete wordpress website template for the tuckwell company

I need a wordpress themed website designed for a new social enterprise who provide healthy catering/food supply to schools. It needs to be the FULL/COMPLETE wordpress theme! I want it to be simple, sleek, easy to use and SEO friendly.

I am going to leave the brief pretty open as I would like to see your ideas.

I am attaching a company logo and would like the design to incorporate the colours but not in an overpowering way. Keep it clean and crisp.

The mission of the company is to provide healthy catering and food supply to students in Irish schools with an emphasis on promoting increased consumption of fruit and veg so please keep this in mind. I would like space for images on main page and lower pages or maybe an image roll but very open here so will welcome your ideas
I want to be able to add tabs to the top level as we introduce new services.
Tabs should include
Home
About us
Our service (split into primary & post primary schools)
Resources again this will be split as above
Links
Contact us
Homepage should include a news section and links to social media being relatively prominent
Updates

Reason: I was requested to extend to allow time for more submissions

I have updated the brief for the project

Thanks

Rob

Reason: this is the last extension of the deadline.  WIll provide feedback on all designs over coming days

Target Market(s)

should appeal to principals, teachers and parents

Industry/Entity Type

Catering

Requirements
Must have
• incorporate logo and this should fit in with overall colour scheme and feel
links for facebook twitter etc must be relatively prominent
Feel like website not a blog
News page on front page possibly all pages
reflect the healthy eating ethos of the company
Nice to have
• contact form istock photos

```html
<!DOCTYPE html>
<html lang="en">
<head>
<meta charset="utf-8">
<title>The Tuckwell Company</title>
<link rel="stylesheet" href="https://fonts.googleapis.com/css2?family=Open+Sans:wght@400;600;700&family=Yanone+Kaffeesatz:wght@400;500&family=Signika:wght@300;400&display=swap">
<style>
:root{
  --green:#6cb21a;
  --green-light:#8fd12a;
  --green-dark:#2f7a0a;
  --nav-dark:#2e6d0c;
  --beige:#ede6c5;
  --orange:#f5951c;
  --orange-dark:#e0640a;
  --blue:#2a8fd8;
  --blue-dark:#1466a8;
  --red-title:#e24a0a;
  --text:#222;
  --soil:#5a3a22;
  --white:#fff;
}
*{box-sizing:border-box;margin:0;padding:0}
html,body{width:999px;height:1200px;overflow:hidden}
body{position:relative;background:var(--white);font-family:Arial,Helvetica,sans-serif;color:var(--text)}
.abs{position:absolute}
.top-line{left:0;top:0;width:999px;height:4px;background:var(--green)}
.call-tab{left:590px;top:4px;width:392px;height:38px;background:linear-gradient(#7cc42a,#4f9a12);border-radius:0 0 8px 18px;color:var(--white);font:700 17px Arial,sans-serif;display:flex;align-items:center;justify-content:center;gap:6px}
.call-tab .q{color:#d9f57a}
.brand{left:35px;top:10px;width:240px;height:115px}
.brand-circle{left:122px;top:0;width:112px;height:112px;border-radius:50%;background:#e4e4e4;border:4px solid #f4f4f4;box-shadow:0 2px 4px rgba(0,0,0,.3)}
.brand-name{left:0;top:38px;width:150px;font:700 22px/1.05 "Open Sans",sans-serif;color:#27a3d9}
.main-nav{left:255px;top:90px;width:727px;height:45px}
.main-nav ul{position:absolute;left:52px;top:15px;list-style:none;display:flex;white-space:nowrap;font:400 12px "Open Sans",sans-serif;color:var(--white)}
.main-nav li+li:before{content:"|";margin:0 10px}
.main-nav .active{color:#39c4f2}
.search{left:520px;top:14px;width:195px;height:20px;background:var(--white);border:1px solid #aaa;font:11px Arial,sans-serif;color:#999;padding:3px 4px}
.hero{left:18px;top:135px;width:965px;height:328px;background:var(--white);box-shadow:0 1px 4px rgba(0,0,0,.35)}
.hero-inner{left:10px;top:10px;width:945px;height:308px;background:#e6e6e6;overflow:hidden}
.hero-photo{left:440px;top:0;width:505px;height:308px;background:linear-gradient(90deg,rgba(230,230,230,1) 0%,rgba(235,200,140,.8) 20%,#e8b04a 45%,#c8702a 65%,#7aa03a 85%,#c23a20 100%)}
.welcome{left:14px;top:24px;font:400 24px "Yanone Kaffeesatz",sans-serif;color:#1e4a12}
.welcome span{color:var(--orange);font-size:26px}
.rule{height:1px;background:#888}
.hero-text{left:17px;top:70px;width:345px;font:11px/14px Arial,sans-serif;letter-spacing:-.1px}
.hero-text p+p{margin-top:14px}
.btn-blue{left:13px;top:234px;width:105px;height:25px;border-radius:3px;background:linear-gradient(#46a9ec,var(--blue-dark));border:1px solid #0d4f86;color:var(--white);font:700 11px/23px Arial,sans-serif;padding-left:12px}
.follow-bar{left:28px;top:462px;width:945px;height:77px;background:linear-gradient(#f4f6f8,#d6e0ea);border:1px solid #c4ced8;border-top:0;border-radius:0 0 10px 10px}
.follow-btn{left:6px;top:25px;width:149px;height:31px;border-radius:4px;background:linear-gradient(#ffb03a,var(--orange-dark));color:var(--white);font:italic 700 17px/31px Arial,sans-serif;text-align:center}
.social{top:20px;width:38px;height:40px;border-radius:7px;background:linear-gradient(#7fc8ee,#2a86c4);box-shadow:0 2px 3px rgba(0,0,0,.3)}
.agent{left:395px;top:405px;width:126px;height:126px;border-radius:50%;border:4px solid var(--white);background:linear-gradient(#d8dde2,#b9c2ca);box-shadow:0 1px 4px rgba(0,0,0,.35)}
.need-help{left:500px;top:474px;width:167px;text-align:right;color:#2d8a0e;font:400 17px Arial,sans-serif;white-space:nowrap}
.need-help b{font:700 22px Arial,sans-serif;color:#3fa812}
.need-help .num{display:block;font:700 22px/24px Arial,sans-serif;color:#3fa812;letter-spacing:-.3px}
.sign-in{left:690px;top:469px;width:277px;height:66px;border-radius:8px;background:linear-gradient(#2d78b8,#14477e);border:2px solid #9fc2e4}
.sign-in h3{position:absolute;left:7px;top:5px;font:300 18px "Signika",sans-serif;color:var(--white)}
.field{background:var(--white);border:1px solid #bbb;font:11px Arial,sans-serif;color:#999;padding:4px 5px}
.go{left:220px;top:30px;width:46px;height:23px;background:linear-gradient(#ffb03a,var(--orange-dark));color:var(--white);font:15px/23px Arial,sans-serif;text-align:center}
.green-field{left:0;top:545px;width:999px;height:580px;background:linear-gradient(#84cc1e,#6ab418 60%,#5da812)}
.panel{background:var(--white);box-shadow:0 1px 3px rgba(0,0,0,.25)}
.panel-inner{background:var(--beige)}
.section-title{font:300 25px "Signika",sans-serif;color:#222;display:flex;align-items:flex-end;gap:6px;white-space:nowrap}
.section-title:after{content:"";flex:1;border-bottom:1px dashed #555;margin-bottom:5px}
.who-text{left:10px;top:55px;width:395px;font:11px/14.5px Arial,sans-serif;color:#c7700a;letter-spacing:-.1px}
.photo{background:linear-gradient(135deg,#3d3a30,#6a5a40 40%,#2f3a2a)}
.btn-orange{height:22px;border-radius:4px;background:linear-gradient(#ff9a2e,var(--orange-dark));border:1px solid #b44a06;color:#3a1a00;font:700 11px/20px Arial,sans-serif;text-align:center}
.card-photo{top:804px;width:223px;height:116px;background:#1f4a12;padding:6px}
.card-photo div{width:100%;height:100%}
.card-title{top:933px;width:219px;font:400 21px "Yanone Kaffeesatz",sans-serif;color:#f4f0a8;letter-spacing:.5px;padding-bottom:3px;border-bottom:1px dashed #2f6a10}
.card-text{top:968px;width:219px;font:11px/14px Arial,sans-serif;color:#1a2a0a;text-align:justify;letter-spacing:-.35px}
.news-item{left:6px;width:232px;font:11px/14px Arial,sans-serif;padding-bottom:8px;border-bottom:1px dashed #c8a860}
.news-item h4{font:700 12px Arial,sans-serif;color:var(--red-title);margin-bottom:3px}
.news-item p{text-decoration:underline}
.news-btn{left:12px;top:319px;width:242px;height:42px;border-radius:5px;background:linear-gradient(#63c8f5,#1e92d0);border:1px solid #1478b0;color:#0a2a44;font:300 25px/40px "Signika",sans-serif;padding-left:13px}
.subscribe{left:717px;top:941px;width:266px;height:158px;background:linear-gradient(#4ea8ee,#1e7fd0);border:2px solid #a8d0f2}
.subscribe h3{position:absolute;left:9px;top:10px;font:300 24px "Signika",sans-serif;color:var(--white)}
.grass{left:0;top:1104px;width:999px;height:24px}
.footer{left:0;top:1124px;width:999px;height:76px;background:linear-gradient(#6a4528,var(--soil) 40%,#4a2e18)}
.footer p{position:absolute;top:38px;width:100%;text-align:center;font:11px Arial,sans-serif;color:var(--white)}
.footer span{margin:0 10px}
</style>
</head>
<body>
<div class="abs top-line"></div>

<div class="abs call-tab"><span class="q">Questions?</span> Call US
  <svg width="22" height="22" viewBox="0 0 24 24"><path d="M6.6 10.8a15 15 0 0 0 6.6 6.6l2.2-2.2c.3-.3.7-.4 1-.2 1.1.4 2.3.6 3.6.6.6 0 1 .4 1 1V20c0 .6-.4 1-1 1A17 17 0 0 1 3 4c0-.6.4-1 1-1h3.5c.6 0 1 .4 1 1 0 1.3.2 2.5.6 3.6.1.3 0 .7-.2 1z" fill="#fff"/></svg>
  555 0134 0134</div>

<header class="abs brand">
  <div class="abs brand-circle"></div>
  <div class="abs brand-name">The Tuckwell Company</div>
</header>

<nav class="abs main-nav">
  <svg class="abs" width="727" height="45"><path d="M0 45 C20 30 35 5 55 0 H720 a7 7 0 0 1 7 7 V45 Z" fill="#2e6d0c"/></svg>
  <ul><li class="active">Home</li><li>About Us</li><li>Our Services</li><li>Resources</li><li>Links</li><li>Contact Us</li></ul>
  <div class="abs search">Type Your keywords here
    <svg class="abs" style="right:4px;top:2px" width="15" height="15" viewBox="0 0 16 16"><circle cx="9.5" cy="6.5" r="4.5" fill="none" stroke="#222" stroke-width="2"/><path d="M6 10 L1.5 14.5" stroke="#222" stroke-width="2.5"/></svg>
  </div>
</nav>

<section class="abs hero">
  <div class="abs hero-inner">
    <div class="abs hero-photo" role="img" aria-label="Photo of fresh melons, grapes, pineapple, apples and other fruit"></div>
    <h1 class="abs welcome">WELCOME TO <span>THE TUCKWELL COMPANY</span></h1>
    <div class="abs rule" style="left:14px;top:58px;width:369px"></div>
    <div class="abs hero-text">
      <p>Lorem ipsum dolor sit amet, consectetur adipiscing elit. Etiam accumsan lorem sit amet lorem fermentum vitae dapibus mi viverra. Cras sagittis consectetur sollicitudin. Proin ultrices turpis at quam aliquet nec condimentum erat consequat. Cras euismod facilisis viverra. Sed diam velit, elementum eu consequat sit amet.</p>
      <p>Proin ultrices turpis at quam aliquet nec condimentum erat consequat. Cras euismod facilisis viverra. Sed diam velit, elementum eu consequat sit amet.</p>
    </div>
    <div class="abs rule" style="left:14px;top:218px;width:369px"></div>
    <div class="abs btn-blue">↳ read more</div>
  </div>
</section>

<section class="abs follow-bar">
  <div class="abs follow-btn">Follow Us On</div>
  <div class="abs social" style="left:169px"></div>
  <div class="abs social" style="left:216px"></div>
  <div class="abs social" style="left:263px"></div>
  <div class="abs social" style="left:310px"></div>
</section>
<div class="abs agent" role="img" aria-label="Photo of a customer support agent wearing a headset"></div>
<div class="abs need-help">need <b>HELP</b><span class="num">555 0134 0134</span></div>

<form class="abs sign-in">
  <h3>Sign In</h3>
  <div class="abs field" style="left:10px;top:31px;width:101px;height:21px">Username</div>
  <div class="abs field" style="left:116px;top:31px;width:101px;height:21px">********</div>
  <div class="abs go">Go</div>
</form>

<div class="abs green-field"></div>

<section class="abs panel" style="left:20px;top:557px;width:692px;height:235px">
  <div class="abs panel-inner" style="left:8px;top:8px;width:676px;height:219px">
    <h2 class="abs section-title" style="left:9px;top:6px;width:660px">Who we are</h2>
    <p class="abs who-text">Lorem ipsum dolor sit amet, consectetur adipiscing elit. Etiam blandit pretium odio, vitae laoreet mauris pretium nec. Suspendisse auctor egestas tincidunt. Pellentesque at neque diam, vitae condimentum felis. Pellentesque a ante mauris. Maecenas ornare massa ut nibh iaculis blandit. Integer augue magna, dapibus ac dignissim ut, molestie eget velit. Proin semper fermentum quam, quis dictum turpis vestibulum sit amet. Praesent congue pulvinar elit, sed convallis sapien egestas auctor. Cras vitae commodo diam.</p>
    <div class="abs photo" style="left:414px;top:43px;width:253px;height:144px;border:1px solid #6a5a30" role="img" aria-label="Photo of a woman unloading crates of fresh vegetables from a van"></div>
    <div class="abs btn-orange" style="left:8px;top:168px;width:86px">read more »</div>
  </div>
</section>

<div class="abs card-photo" style="left:20px"><div style="background:linear-gradient(135deg,#f2f2ee,#d8b890 50%,#b8502a)" role="img" aria-label="Photo of a wrap sandwich with tomatoes"></div></div>
<div class="abs card-photo" style="left:253px"><div style="background:linear-gradient(135deg,#c8b088,#e0783a 50%,#3a6a20)" role="img" aria-label="Photo of fresh carrots and parsnips"></div></div>
<div class="abs card-photo" style="left:486px"><div style="background:linear-gradient(135deg,#f08a20,#e8c040 45%,#c43a20 75%,#b8c858)" role="img" aria-label="Photo of oranges, pears, apples and grapes"></div></div>

<h3 class="abs card-title" style="left:22px">HYGENIC FOOD</h3>
<h3 class="abs card-title" style="left:255px">FRESH VEGETABLES</h3>
<h3 class="abs card-title" style="left:488px">ALL SEASON FRUITS</h3>

<p class="abs card-text" style="left:22px">Phasellus arcu metus, aliquam in dignissim ut, posuere eu est. Aenean elit ligula, iaculis eu tincidunt id, ultricies vitae nisl. Nunc iaculis tempus nisl. Vivamus vitae sem a risus volutpat commodo. Sed ac enim mi. Quisque</p>
<p class="abs card-text" style="left:255px">Phasellus arcu metus, aliquam in dignissim ut, posuere eu est. Aenean elit ligula, iaculis eu tincidunt id, ultricies vitae nisl. Nunc iaculis tempus nisl. Vivamus vitae sem a risus volutpat commodo. Sed ac enim mi. Quisque</p>
<p class="abs card-text" style="left:488px">Phasellus arcu metus, aliquam in dignissim ut, posuere eu est. Aenean elit ligula, iaculis eu tincidunt id, ultricies vitae nisl. Nunc iaculis tempus nisl. Vivamus vitae sem a risus volutpat commodo. Sed ac enim mi. Quisque</p>

<div class="abs btn-orange" style="left:22px;top:1053px;width:85px">read more »</div>
<div class="abs btn-orange" style="left:254px;top:1053px;width:85px">read more »</div>
<div class="abs btn-orange" style="left:487px;top:1053px;width:85px">read more »</div>

<aside class="abs panel" style="left:718px;top:557px;width:265px;height:375px">
  <div class="abs panel-inner" style="left:8px;top:6px;width:250px;height:362px">
    <h2 class="abs section-title" style="left:5px;top:4px;width:238px">Latest News</h2>
    <div class="abs news-item" style="top:52px"><h4>Lorem Ipsum Dolor Sit Amet,</h4><p>Aliquam eget sem et quam ultricies facilisis et sit amet ligula. Nam sed est vitae quam ornare tristique vel eu leo. Ut consequat rhoncus mi.</p></div>
    <div class="abs news-item" style="top:140px"><h4>Lorem Ipsum Dolor Sit Amet,</h4><p>Aliquam eget sem et quam ultricies facilisis et sit amet ligula. Nam sed est vitae quam ornare tristique vel eu leo. Ut consequat rhoncus mi.</p></div>
    <div class="abs news-item" style="top:227px"><h4>Lorem Ipsum Dolor Sit Amet,</h4><p>Aliquam eget sem et quam ultricies facilisis et sit amet ligula. Nam sed est vitae quam ornare tristique vel eu leo. Ut consequat rhoncus mi.</p></div>
  </div>
  <div class="abs news-btn">Read More News
    <svg class="abs" style="right:12px;top:15px" width="30" height="12" viewBox="0 0 30 12"><path d="M2 1l5 5-5 5M11 1l5 5-5 5M20 1l5 5-5 5" fill="none" stroke="#fff" stroke-width="3"/></svg>
  </div>
</aside>

<form class="abs subscribe">
  <h3>Subscribe Newsletter</h3>
  <div class="abs field" style="left:10px;top:50px;width:237px;height:27px;line-height:17px">Your Name</div>
  <div class="abs field" style="left:10px;top:87px;width:237px;height:27px;line-height:17px">Your email id</div>
  <div class="abs btn-orange" style="left:11px;top:123px;width:92px;height:27px;line-height:25px;color:#1a0a00">Subscribe ⁘</div>
</form>

<svg class="abs grass" viewBox="0 0 999 24" preserveAspectRatio="none"><path d="M0 24V10l8-6 6 5 7-7 6 6 8-5 5 4 9-6 6 7 7-5 8 4 6-6 7 7 8-5 6 4 7-6 9 6 6-5 7 5 8-7 6 6 7-4 8 5 6-7 7 6 9-5 6 5 7-6 8 6 6-4 7 4 8-7 6 7 7-5 9 5 6-6 7 6 8-5 6 5 7-7 8 6 6-4 7 5 9-6 6 6 7-5 8 5 6-7 7 6 8-4 6 4 7-6 9 6 6-5 7 5 8-7 6 6 7-4 8 5 6-7 7 6 9-5 6 5 7-6 8 6 6-4 7 4 8-7 6 7 7-5 9 5 6-6 7 6 8-5 6 5 7-7 8 6 6-4 7 5 9-6 6 6 7-5 8 5 6-7 7 6 8-4 6 4 7-6 9 6 6-5 7 5 8-7 6 6 7-4 8 5 6-7 7 6 9-5 6 5 7-6 8 6 6-4 7 4 8-7 6 7 7-5 9 5 6-6 7 6 8-5 6 5 7-7 8 6 6-4 7 5 9-6 6 6 7-5 8 5 6-7 7 6 8-4 6 4 7-6 9 6 6-5 7 5 8-7 6 6 7-4 8 5 6-7 7 6 9-5 6 5 7-6 8 6 6-4 7 4 8-7 6 7 7-5 9 5 6-6 7 6 8-5 6 5 7-7 8 6 6-4 7 5 9-6 6 6 7-5 8 5 6-7 7 6 8-4 6 4 7-6 9 6 6-5 7 5 8-7 6 6 7-4 8 5 6-7 7 6 9-5 6 5 7-6 8 6 6-4 7 4 8-7 6 7 7-5 9 5 6-6 7 6 8-5 6 5 L999 10V24Z" fill="#9ad83a"/></svg>

<footer class="abs footer">
  <p>©2010-2011, All Rights Reserved, thetuckwellcompany<span>|</span>Privacy Policy<span>|</span>Terms &amp; Conditions</p>
</footer>
</body>
</html>
```